Name Card Design Project for a Japanese Restaurant

We need a name card design for our company. We run traditional japanese restaurant(Izakaya Concept) in singapore. We have 3 branches and one HQ. We would like to see designs that use the bright colour. Please visit
http://plimtarn.com/harusemi/ for our coming new website

Name Card 1:
Name: Tode Kinji
Position: Managing Director
Email Add: tode@harusemi.com.sg

Name Card 2: Name: Dorinda Poh
Postion: Operation Manager
Email Add: dorinda@harusemi.com.sg

Name Card 3:
Name: Gilbert Poh
Position: Office Manager
Email Add: gilbert@harusemi.com.sg

Name Card 4:
Name: Kitamo Sei
Position: Executive Chef
Email Add: Leave it blank

Name Card 5:
Name: Tsumeda Ayaka
Position: Executive Chef
Email Add: Leave it blank

Name Card 6:
Name: Leave it blank
Position: Leave it blank
Email Add: Leave it blank

Font Side:
Company Name: Harusemi Restaurant (Mellow Hill) Pte Ltd
Name:
Position:
Email Add:
Address: 37 Pelling Road #04-27 Singapore 051238
Tel: (65)64718352
Fax:(65) 64718397
Website: www.harusemi.com.sg

Back Side:
Jurong Branch:
9 Lorimer Drive #01-05B
Singapore 627315
(Glintlane)
Tel: 67305418

Corvick Street Branch:
6 Corvick Street #01-12/15
Singapore 057293
(Bedok Marrin Exit C)
Tel:69142703

Balestier Branch:
14 Teck Lim Road #01-09
(Meilin Court)
Singapore 316457
**New Outlet

Log in www.harusemi.com.sg for Bento Delivery Service
Updates

There is a typo mistake in the logo. Please use this to replace. Thanks 

      https://www.fernsharebox.com/sh/3kqwzm82plr04vt/QJtrHxLaMc

Target Market(s)

working class people (weekdays) and family (weekends)

Industry/Entity Type

Restaurant

Requirements
Must have
• The name cards must use the logo we have attached

```html
<!DOCTYPE html>
<html lang="en">
<head>
<meta charset="utf-8">
<title>Harusemi Japanese Restaurant – Name Cards</title>
<link rel="stylesheet" href="https://fonts.googleapis.com/css2?family=Didact+Gothic&family=Rowdies:wght@400&family=Lora:ital,wght@1,600&display=swap">
<style>
  :root{
    --page:#ffffff;
    --cream-light:#f3ead4;
    --cream:#e6d7b2;
    --red:#d7202c;
    --red-deep:#b8141f;
    --red-soft:#e0505a;
    --ink:#1c1414;
    --grey:#4a4444;
    --paper:#fbfbfa;
    --bamboo:#d6bf8f;
    --bamboo-edge:#b79f6d;
    --white:#ffffff;
  }
  *{box-sizing:border-box;margin:0;padding:0}
  html,body{width:1200px;height:1000px;overflow:hidden;background:var(--page)}
  body{position:relative;font-family:"Didact Gothic",sans-serif;color:var(--grey)}

  .card{position:absolute;top:344px;width:520px;height:312px;overflow:hidden;
        box-shadow:0 1px 3px rgba(0,0,0,.18)}
  .card--front{left:40px}
  .card--back{left:640px;background:var(--paper)}

  .brand-panel{position:absolute;left:0;top:0;bottom:0;width:148px;
        background:linear-gradient(180deg,var(--cream-light),var(--cream))}
  .card--back .brand-panel{width:152px}

  .brand{position:absolute;left:0;right:0;top:32px;display:flex;flex-direction:column;align-items:center;gap:10px}
  .brand__dot{width:54px;height:54px;border-radius:50%;background:var(--red)}
  .brand__name{font-family:"Rowdies",sans-serif;font-size:19px;color:var(--ink);letter-spacing:.5px}

  .hq-address{position:absolute;left:0;right:0;top:178px;text-align:center;
        font-size:14.5px;line-height:17px;color:var(--grey)}

  .red-field{position:absolute;left:148px;top:0;right:0;bottom:0;
        background:linear-gradient(160deg,var(--red-deep) 0%,var(--red) 55%,var(--red-soft) 100%)}

  .person{position:absolute;left:168px;top:146px;color:var(--white)}
  .person__name{font-family:"Rowdies",sans-serif;font-size:17px}
  .person__role{font-size:15px;margin-top:2px;opacity:.92}

  .contact{position:absolute;right:22px;top:218px;text-align:right;color:var(--white);font-size:14.5px;line-height:18px}
  .contact__company{position:absolute;left:168px;top:212px;font-family:"Rowdies",sans-serif;font-size:11.5px;color:var(--white);white-space:nowrap;text-transform:uppercase}
  .contact__lines{margin-top:14px}
  .contact__web{font-family:"Lora",serif;font-style:italic;font-weight:600;font-size:13px;line-height:17px;margin-top:2px}

  .branch-col{position:absolute;top:0;bottom:0}
  .branch-col--mid{left:152px;width:172px;padding:48px 0 0 18px}
  .branch-col--right{left:324px;right:0;padding:0 0 0 18px}

  .chopstick{position:absolute;top:22px;bottom:14px;width:5px;border-radius:3px;
        background:linear-gradient(90deg,var(--bamboo),var(--bamboo-edge))}
  .chopstick--a{left:316px}
  .chopstick--b{left:496px;top:62px}

  .branch{font-size:13px;line-height:15.5px;color:var(--grey)}
  .branch + .branch{margin-top:10px}
  .branch__title{font-family:"Rowdies",sans-serif;font-size:11px;color:var(--red);text-transform:uppercase;margin-bottom:2px;letter-spacing:.3px}

  .delivery{position:absolute;left:336px;top:28px;width:148px;height:148px;border-radius:50%;background:var(--red);
        display:flex;flex-direction:column;align-items:center;justify-content:center;text-align:center;
        font-family:"Rowdies",sans-serif;font-size:11.5px;line-height:15px;color:var(--white);text-transform:uppercase}
  .delivery__url{font-family:"Lora",serif;font-style:italic;font-weight:600;text-transform:none;font-size:11.5px}

  .branch--balestier{position:absolute;left:342px;top:184px}
</style>
</head>
<body>

  <section class="card card--front" aria-label="Name card front">
    <div class="brand-panel">
      <div class="brand">
        <span class="brand__dot"></span>
        <span class="brand__name">HARUSEMI</span>
      </div>
      <p class="hq-address">37 Pelling Road<br>#04-27<br>Singapore<br>051238</p>
    </div>
    <div class="red-field" role="img" aria-label="Red background with a soft Japanese diamond motif"></div>
    <div class="person">
      <p class="person__name">Tode Kinji</p>
      <p class="person__role">Managing Director</p>
    </div>
    <p class="contact__company">Harusemi Restaurant (Mellow Hill) Pte Ltd</p>
    <div class="contact">
      <div class="contact__lines">
        <p>t.(65) 64718352</p>
        <p>f.(65) 64718397</p>
      </div>
      <p class="contact__web">tode@harusemi.com.sg</p>
      <p class="contact__web">www.harusemi.com.sg</p>
    </div>
  </section>

  <section class="card card--back" aria-label="Name card back">
    <div class="brand-panel">
      <div class="brand">
        <span class="brand__dot"></span>
        <span class="brand__name">HARUSEMI</span>
      </div>
    </div>

    <span class="chopstick chopstick--a"></span>
    <span class="chopstick chopstick--b"></span>

    <div class="branch-col branch-col--mid">
      <div class="branch">
        <p class="branch__title">Jurong Branch</p>
        <p>9 Lorimer Drive<br>#01-05B<br>Singapore 627315<br>(Glintlane)<br>t. 67305418</p>
      </div>
      <div class="branch">
        <p class="branch__title">Corvick Street Branch</p>
        <p>6 Corvick Street<br>#01-12/15<br>Singapore 057293<br>(Bedok Marrin Exit C)<br>t. 69142703</p>
      </div>
    </div>

    <div class="delivery">
      <p>Log in</p>
      <p class="delivery__url">www.harusemi.com.sg</p>
      <p>for Bento<br>Delivery Service</p>
    </div>

    <div class="branch branch--balestier">
      <p class="branch__title">Balestier Branch</p>
      <p>14 Teck Lim Road<br>#01-09<br>(Meilin Court)<br>Singapore<br>316457</p>
    </div>
  </section>

</body>
</html>
```